Research and Development Technical Training for Process Engineering

We are creating a TeamPortal site that will contain links to several training materials. I will create and upload the content, just looking for graphics and a basic layout for a single homepage. The page should contain unique graphics for the following topics/categories: Methodology, Equipment Training, Design References, Safety & Environmental, and Technology. (See attached example. Layout example DOES NOT need to be followed, only an example).
Also, a graphic to be used for a Powerpoint template that is cohesive with the graphics previously mentioned. Space for a company logo required. Professional/business application. Company logo already exists, it is blue and red but these colors are not required to be used as a theme.
Industry/Entity Type
Training
Number of Pages Required
1 page
Colors
Designer to choose colors to be used in the design.
Look and feel

```html
<!DOCTYPE html>
<html lang="en">
<head>
<meta charset="utf-8">
<title>Research &amp; Development Training</title>
<link rel="stylesheet" href="https://fonts.googleapis.com/css2?family=Montserrat:wght@600;700&family=Carlito:wght@400;700&display=swap">
<style>
  :root {
    --frame: #e4e4e6;
    --navy: #26297a;
    --navy-deep: #0b0b6e;
    --brand-red: #e5322d;
    --blue: #1a6fc0;
    --blue-dark: #155fa8;
    --heading-blue: #1c66b0;
    --text: #3a3a3a;
    --panel: #f2f2f3;
    --white: #ffffff;
    --maroon: #a3124b;
    --orange: #f27812;
    --pink: #cf659d;
    --teal: #139ea6;
    --black: #111111;
    --icon-indigo: #30326f;
    --icon-blue: #2a5fd4;
    --icon-purple: #6b2a77;
    --icon-green: #1f7a4f;
    --icon-red: #8e1e24;
  }
  * { box-sizing: border-box; margin: 0; padding: 0; }
  html, body { width: 1000px; height: 1200px; overflow: hidden; }
  body { background: var(--frame); font-family: "Carlito", "Calibri", sans-serif; position: relative; }

  .page { position: absolute; left: 11px; top: 11px; width: 978px; height: 1178px; background: var(--white); overflow: hidden; }

  .hero { position: absolute; left: 0; top: 0; width: 978px; height: 192px; }
  .hero-photo { position: absolute; inset: 0;
    background: linear-gradient(100deg, #3a3d8c 0%, #4b4fa0 40%, #3f4398 70%, #2c2f86 100%); }
  .hero-title { position: absolute; left: 99px; top: 86px; font-family: "Montserrat", sans-serif; font-weight: 600;
    font-size: 21px; letter-spacing: 0.3px; color: var(--white); }
  .brand-corner { position: absolute; right: 0; top: 0; width: 341px; height: 96px; }
  .brand-name { position: absolute; left: 773px; top: 35px; font-family: "Montserrat", sans-serif; font-weight: 700;
    font-size: 29px; letter-spacing: 1px; color: var(--brand-red); }

  .intro { position: absolute; left: 0; top: 192px; width: 978px; height: 320px;
    background: linear-gradient(160deg, #ffffff 45%, #eef5f6 70%, #ffffff 90%); }
  .product-tile { position: absolute; left: 51px; top: 63px; width: 165px; height: 122px; background: var(--blue);
    display: flex; align-items: center; justify-content: center; gap: 8px; color: var(--white);
    font-family: "Montserrat", sans-serif; font-weight: 700; font-size: 15px; letter-spacing: 0.5px; }
  .product-tile .mark { width: 14px; height: 14px; background: var(--white); }
  .intro-heading { position: absolute; left: 242px; top: 74px; font-family: "Montserrat", sans-serif; font-weight: 600;
    font-size: 19px; color: var(--heading-blue); letter-spacing: 0.2px; }
  .intro-copy { position: absolute; left: 241px; top: 111px; width: 700px; font-size: 14.2px; line-height: 18.5px; color: var(--text); }
  .learn-more { position: absolute; left: 240px; top: 420px; top: 239px; width: 152px; height: 30px; border-radius: 15px;
    background: var(--blue); color: var(--white); font-size: 14px; font-weight: 700; padding-left: 13px; line-height: 30px; }
  .learn-more .go { position: absolute; right: 7px; top: 5px; width: 20px; height: 20px; }

  .topics { position: absolute; left: 0; top: 512px; width: 978px; height: 639px; background: var(--panel); }
  .card { position: absolute; width: 276px; height: 244px; border-radius: 5px; overflow: hidden;
    box-shadow: 0 0 0 2px var(--white); }
  .card-photo { position: absolute; inset: 0; }
  .card-icon { position: absolute; left: 100px; top: 38px; width: 76px; height: 76px; border-radius: 50%;
    border: 4px solid rgba(220,220,225,0.9); display: flex; align-items: center; justify-content: center; }
  .card-title { position: absolute; left: 0; right: 0; top: 124px; text-align: center; font-family: "Montserrat", sans-serif;
    font-weight: 600; font-size: 13.5px; color: var(--white); letter-spacing: 0.2px; text-shadow: 0 1px 2px rgba(0,0,0,0.5); }
  .card-text { position: absolute; left: 12px; right: 12px; top: 141px; text-align: center; font-size: 13.6px;
    line-height: 16.8px; color: var(--white); text-shadow: 0 1px 2px rgba(0,0,0,0.55); }
  .card-corner { position: absolute; right: 0; bottom: 0; width: 50px; height: 50px; border-top-left-radius: 50px;
    border-top: 2px solid var(--white); border-left: 2px solid var(--white); }
  .card-corner svg { position: absolute; right: 12px; bottom: 12px; }

  .footer { position: absolute; left: 0; top: 1151px; width: 978px; height: 27px; background: var(--navy-deep);
    color: var(--white); font-family: "Carlito", sans-serif; font-weight: 700; font-size: 10.5px; text-align: center; line-height: 27px; }
</style>
</head>
<body>
<div class="page">
  <header class="hero">
    <div class="hero-photo" role="img" aria-label="Photo of a smiling team in a meeting, tinted deep blue"></div>
    <h1 class="hero-title">RESEARCH &amp; DEVELOPMENT TRAINING</h1>
    <svg class="brand-corner" viewBox="0 0 341 96" aria-hidden="true"><polygon points="0,0 341,0 341,96 84,96" fill="#ffffff"/></svg>
    <div class="brand-name">VANTEX</div>
  </header>

  <section class="intro">
    <div class="product-tile"><span class="mark"></span>TEAMPORTAL</div>
    <h2 class="intro-heading">TEAMPORTAL</h2>
    <p class="intro-copy">Lorem ipsum dolor sit amet, consectetuer adipiscing elit, sed diam nonummy nibh euismod tincidunt ut laoreet dolore ma na aliquam erat volutpat. Ut wisi enim ad minim veniam, quis nostrud exerci tation ullamcorper suscipit lobortis nisl ut ali quip ex ea commodo consequat. Duis autem vel eum iriure dolor in hendrerit in vulputate velit esse molestie consequat, vel illum dolore eu feugiat nulla facilisis at vero eros et accumsan et iusto odio dignissim qui blandit praesent luptatum zzr il delenit augue duis dolore te feugait nulla facilisi.</p>
    <div class="learn-more">Learn More
      <svg class="go" viewBox="0 0 20 20" aria-hidden="true"><circle cx="10" cy="10" r="8.5" fill="none" stroke="#fff" stroke-width="1.4"/><path d="M7 13 L13 7 M9 7 H13 V11" stroke="#fff" stroke-width="1.6" fill="none"/></svg>
    </div>
  </section>

  <section class="topics">
    <article class="card" style="left:51px; top:74px;">
      <div class="card-photo" role="img" aria-label="Photo of a team meeting around a conference table" style="background:linear-gradient(160deg,#c9ccd0 0%,#8d9096 50%,#6f6c68 100%);"></div>
      <div class="card-icon" style="background:var(--icon-indigo);">
        <svg width="42" height="42" viewBox="0 0 42 42" aria-hidden="true" fill="#fff"><rect x="3" y="3" width="13" height="13"/><rect x="26" y="3" width="13" height="13"/><rect x="3" y="26" width="13" height="13"/><rect x="26" y="26" width="13" height="13"/><path d="M17 9 H24 M9 17 V24 M17 33 H24 M33 17 V24" stroke="#fff" stroke-width="2"/></svg>
      </div>
      <h3 class="card-title">METHODOLOGY</h3>
      <p class="card-text">Lorem ipsum dolor sit amet, consectetuer adipiscing elit, sed diam nonummy nibheu ismod tincidunt ut laoreet dolore magna.</p>
      <div class="card-corner" style="background:var(--maroon);"><svg width="20" height="20" viewBox="0 0 20 20" aria-hidden="true"><circle cx="10" cy="10" r="8.5" fill="none" stroke="#fff" stroke-width="1.4"/><path d="M7 13 L13 7 M9 7 H13 V11" stroke="#fff" stroke-width="1.6" fill="none"/></svg></div>
    </article>

    <article class="card" style="left:351px; top:74px;">
      <div class="card-photo" role="img" aria-label="Photo of hands working on a tablet at a desk" style="background:linear-gradient(160deg,#4f5a68 0%,#7a7466 50%,#8a7454 100%);"></div>
      <div class="card-icon" style="background:var(--icon-blue);">
        <svg width="40" height="40" viewBox="0 0 40 40" aria-hidden="true" fill="none" stroke="#fff" stroke-width="2"><rect x="8" y="6" width="24" height="28" rx="2"/><path d="M12 12 H28 M12 17 H28"/><rect x="12" y="22" width="16" height="7"/><path d="M4 12 H8 M4 20 H8 M4 28 H8 M32 12 H36 M32 20 H36 M32 28 H36"/></svg>
      </div>
      <h3 class="card-title">EQUIPMENT</h3>
      <p class="card-text">Lorem ipsum dolor sit amet, consectetuer adipiscing elit, sed diam nonummy nibheu ismod tincidunt ut laoreet dolore magna.</p>
      <div class="card-corner" style="background:var(--orange);"><svg width="20" height="20" viewBox="0 0 20 20" aria-hidden="true"><circle cx="10" cy="10" r="8.5" fill="none" stroke="#fff" stroke-width="1.4"/><path d="M7 13 L13 7 M9 7 H13 V11" stroke="#fff" stroke-width="1.6" fill="none"/></svg></div>
    </article>

    <article class="card" style="left:651px; top:74px;">
      <div class="card-photo" role="img" aria-label="Photo of a hand over design documents with chart overlay" style="background:linear-gradient(160deg,#7a8090 0%,#9a9ba0 50%,#8a8078 100%);"></div>
      <div class="card-icon" style="background:var(--icon-purple);">
        <svg width="40" height="40" viewBox="0 0 40 40" aria-hidden="true" fill="none" stroke="#fff" stroke-width="3"><path d="M8 26 V8 H26"/><rect x="15" y="15" width="18" height="18"/><rect x="21" y="21" width="6" height="6" stroke-width="2"/></svg>
      </div>
      <h3 class="card-title">DESIGN REFERENCES</h3>
      <p class="card-text">Lorem ipsum dolor sit amet, consectetuer adipiscing elit, sed diam nonummy nibheu ismod tincidunt ut laoreet dolore magna.</p>
      <div class="card-corner" style="background:var(--pink);"><svg width="20" height="20" viewBox="0 0 20 20" aria-hidden="true"><circle cx="10" cy="10" r="8.5" fill="none" stroke="#fff" stroke-width="1.4"/><path d="M7 13 L13 7 M9 7 H13 V11" stroke="#fff" stroke-width="1.6" fill="none"/></svg></div>
    </article>

    <article class="card" style="left:201px; top:343px;">
      <div class="card-photo" role="img" aria-label="Photo of a wind turbine over green fields at dusk" style="background:linear-gradient(180deg,#6a6e78 0%,#8e8a80 45%,#6a7448 80%,#4e6a30 100%);"></div>
      <div class="card-icon" style="background:var(--icon-green);">
        <svg width="40" height="40" viewBox="0 0 40 40" aria-hidden="true"><path d="M20 4 L34 9 V19 C34 28 27 34 20 37 C13 34 6 28 6 19 V9 Z" fill="#fff"/><path d="M20 8 V20 H10 C10 26 14 30 20 33 Z M20 20 H30 V11 L20 8 Z" fill="var(--icon-green)"/></svg>
      </div>
      <h3 class="card-title">SAFETY &amp; ENVIRONMENTAL</h3>
      <p class="card-text">Lorem ipsum dolor sit amet, consectetuer adipiscing elit, sed diam nonummy nibheu ismod tincidunt ut laoreet dolore magna.</p>
      <div class="card-corner" style="background:var(--teal);"><svg width="20" height="20" viewBox="0 0 20 20" aria-hidden="true"><circle cx="10" cy="10" r="8.5" fill="none" stroke="#fff" stroke-width="1.4"/><path d="M7 13 L13 7 M9 7 H13 V11" stroke="#fff" stroke-width="1.6" fill="none"/></svg></div>
    </article>

    <article class="card" style="left:501px; top:343px;">
      <div class="card-photo" role="img" aria-label="Photo of hands holding a tablet showing charts" style="background:linear-gradient(160deg,#a8acb4 0%,#8a8c94 50%,#6c6e78 100%);"></div>
      <div class="card-icon" style="background:var(--icon-red);">
        <svg width="42" height="42" viewBox="0 0 42 42" aria-hidden="true" fill="none" stroke="#fff" stroke-width="2.5"><circle cx="15" cy="16" r="6"/><path d="M15 6 V9 M15 23 V26 M5 16 H8 M22 16 H25 M8 9 L10 11 M20 21 L22 23 M8 23 L10 21 M20 11 L22 9"/><circle cx="29" cy="28" r="4.5"/><path d="M29 20 V23 M29 33 V36 M21 28 H24 M34 28 H37"/></svg>
      </div>
      <h3 class="card-title">TECHNOLOGY</h3>
      <p class="card-text">Lorem ipsum dolor sit amet, consectetuer adipiscing elit, sed diam nonummy nibheu ismod tincidunt ut laoreet dolore magna.</p>
      <div class="card-corner" style="background:var(--black);"><svg width="20" height="20" viewBox="0 0 20 20" aria-hidden="true"><circle cx="10" cy="10" r="8.5" fill="none" stroke="#fff" stroke-width="1.4"/><path d="M7 13 L13 7 M9 7 H13 V11" stroke="#fff" stroke-width="1.6" fill="none"/></svg></div>
    </article>
  </section>

  <footer class="footer">COPYRIGHT © 2018 TEAMPORTAL. ALL RIGHTS RESERVED.</footer>
</div>
</body>
</html>
```